Webpage

I am a professional genealogist. I need a webpage that is professional looking (using the logo I chose), I can add hyperlinks and photos to if and when I want.

```html
<!DOCTYPE html>
<html lang="en">
<head>
<meta charset="utf-8">
<title>Hollow Oak Research</title>
<link rel="stylesheet" href="https://fonts.googleapis.com/css2?family=Questrial&family=Open+Sans:wght@400;600;700&display=swap">
<style>
:root{
  --teal:#12bfd6;
  --teal-dark:#0aa4bd;
  --teal-text:#19a5bf;
  --nav-active:#6fd3e2;
  --footer:#0a9fc7;
  --footer-bar:#087aa0;
  --page-bg:#f6f6f6;
  --ink:#444;
  --muted:#8c8c8c;
  --icon-bg:#4a4e55;
  --field-border:#c9c9c9;
}
*{box-sizing:border-box;margin:0;padding:0}
html,body{width:842px;height:1200px;overflow:hidden;background:#fff}
body{font-family:"Open Sans",Arial,sans-serif;color:var(--ink)}
.page{position:relative;width:842px;height:1200px;overflow:hidden;background:var(--page-bg)}
.abs{position:absolute}

/* header */
.site-header{position:absolute;left:0;top:0;width:842px;height:98px;background:#fff}
.brand{left:78px;top:22px;display:flex;align-items:center;gap:10px}
.brand-mark{width:46px;height:46px;border-radius:50%;background:#bfe6df}
.brand-name{font-family:"Questrial",sans-serif;font-size:17px;color:#333;line-height:1.1}
.question{left:484px;top:20px;font-size:10px;color:#333}
.phone-main{left:484px;top:36px;display:flex;align-items:center;gap:8px}
.phone-badge{width:26px;height:26px;background:var(--teal);border-radius:3px;display:flex;align-items:center;justify-content:center}
.phone-main span{font-family:"Questrial",sans-serif;font-size:17px;color:var(--teal-text)}
.header-address{left:642px;top:24px;font-size:9.5px;line-height:12px;color:#555;text-transform:uppercase;letter-spacing:.2px}

/* nav */
.main-nav{left:70px;top:80px;width:702px;height:34px;background:linear-gradient(#1fc6dc,#0db2cc);border-radius:4px 6px 6px 4px;display:flex;z-index:3}
.main-nav a{display:block;height:34px;line-height:34px;color:#fff;font-size:12px;text-decoration:none;text-align:center;border-right:1px solid rgba(255,255,255,.35);letter-spacing:.3px}
.main-nav a.is-active{background:var(--nav-active);color:#1d5b66;border-radius:4px 0 0 4px}

/* hero */
.hero{left:0;top:98px;width:842px;height:281px;background:linear-gradient(100deg,#c9ccce 0%,#e9ecee 30%,#dfe3e6 55%,#b7c0c6 100%)}
.hero-shadow{left:190px;top:376px;width:506px;height:14px;border-radius:50%;background:radial-gradient(ellipse at center,rgba(0,0,0,.28),rgba(0,0,0,0) 70%)}

/* services */
.service{width:240px;text-align:center}
.service-icon{width:72px;height:72px;border-radius:50%;background:var(--icon-bg);margin:0 auto;display:flex;align-items:center;justify-content:center}
.service-title{font-family:"Questrial",sans-serif;font-size:16.5px;color:var(--teal-text);margin-top:17px;letter-spacing:.5px;white-space:nowrap}
.read-more{display:inline-block;margin-top:12px;width:78px;height:24px;line-height:24px;background:var(--teal);color:#fff;font-size:12px;font-weight:600;text-decoration:none}
.divider{left:240px;top:584px;width:354px;border-top:2px dotted #bbb}

/* welcome */
.welcome-title{left:71px;top:619px;font-family:"Questrial",sans-serif;font-size:17px;font-weight:400;color:var(--teal-text);letter-spacing:.3px}
.welcome-text{left:71px;top:656px;width:433px;font-size:10px;line-height:15.4px;color:var(--muted);text-align:justify}
.map{left:71px;top:772px;width:433px;height:144px;background:linear-gradient(135deg,#e9e5dc 0%,#d9d5cb 45%,#a9c8e6 60%,#e8e4da 100%)}
.contact-row{left:71px;top:926px;display:flex;align-items:flex-start;gap:10px;font-size:9.5px;color:#555;line-height:12px}
.contact-row .ic{width:12px;height:12px}

/* booking */
.booking{left:548px;top:620px;width:224px;height:346px;background:#fff;border:1px solid #e2e2e2}
.booking-head{height:36px;background:var(--teal);color:#fff;font-family:"Questrial",sans-serif;font-size:17px;text-align:center;line-height:36px;letter-spacing:.5px;position:relative}
.booking-head::after{content:"";position:absolute;left:50%;bottom:-7px;margin-left:-8px;border-left:8px solid transparent;border-right:8px solid transparent;border-top:7px solid var(--teal)}
.booking-body{padding:12px 19px 0}
.field-label{font-size:8.5px;color:#666;text-transform:uppercase;letter-spacing:.3px}
.radio-row{display:flex;gap:12px;font-size:10.5px;margin:8px 0 12px;align-items:center}
.radio-row i{display:inline-block;width:10px;height:10px;border:1px solid #999;border-radius:50%;margin-left:4px;vertical-align:-1px}
.input{height:28px;border:1px solid var(--field-border);margin-bottom:6px;font-size:10px;color:#777;padding:0 8px;line-height:26px}
.select-row{display:flex;gap:5px;margin:6px 0 8px}
.select{height:28px;border:1px solid var(--field-border);font-size:10px;color:#555;padding-left:6px;line-height:26px;position:relative;flex:1}
.select::after{content:"";position:absolute;right:6px;top:12px;border-left:4px solid transparent;border-right:4px solid transparent;border-top:4px solid #444}
.book-btn{display:inline-block;margin-top:10px;width:130px;height:31px;line-height:31px;text-align:center;background:var(--teal);color:#fff;font-size:12px;letter-spacing:.3px}

/* footer */
.site-footer{left:0;top:988px;width:842px;height:184px;background:var(--footer);color:#fff}
.footer-title{font-family:"Questrial",sans-serif;font-size:13px;text-transform:uppercase}
.quick-links{left:110px;top:26px}
.quick-links ul{list-style:none;margin-top:10px}
.quick-links li{font-size:9.5px;font-weight:600;line-height:16px;padding-left:9px;position:relative}
.quick-links li::before{content:"›";position:absolute;left:0;color:#bfe8f3}
.connect{left:276px;top:26px;width:230px}
.connect p{font-size:9.5px;font-weight:600;line-height:15px;margin:10px 0 8px}
.social{display:flex;align-items:center;gap:10px;font-size:10px;margin-bottom:9px;text-transform:uppercase}
.social b{width:13px;height:13px;background:#1c6e97;display:inline-block}
.email-form{left:546px;top:26px;width:196px;height:160px}
.email-form .footer-title{text-transform:none;font-size:13px}
.f-input{height:24px;background:#eaeaea;margin-top:6px;font-size:10px;color:#aaa;padding:0 6px;line-height:24px}
.f-input.tall{height:46px}
.submit{position:absolute;right:0;top:138px;width:48px;height:20px;background:#333;color:#fff;font-size:9.5px;text-align:center;line-height:20px}
.footer-bar{left:0;top:1172px;width:842px;height:28px;background:var(--footer-bar);color:#fff;font-size:9px;text-align:center;line-height:28px}
</style>
</head>
<body>
<div class="page">

  <header class="site-header">
    <div class="abs brand">
      <div class="brand-mark"></div>
      <div class="brand-name">Hollow Oak Research</div>
    </div>
    <div class="abs question">Have a question?</div>
    <div class="abs phone-main">
      <div class="phone-badge">
        <svg width="14" height="14" viewBox="0 0 24 24"><path fill="#fff" d="M6.6 10.8a15 15 0 0 0 6.6 6.6l2.2-2.2c.3-.3.7-.4 1-.2 1.1.4 2.3.6 3.6.6.6 0 1 .4 1 1V20c0 .6-.4 1-1 1A17 17 0 0 1 3 4c0-.6.4-1 1-1h3.5c.6 0 1 .4 1 1 0 1.3.2 2.5.6 3.6.1.3 0 .7-.2 1z"/></svg>
      </div>
      <span>+123 555 01842</span>
    </div>
    <div class="abs header-address">Mara Quillen, Professional<br>Genealogist PO Box 4471<br>Riverton, TX 78000-4471</div>
  </header>

  <nav class="abs main-nav">
    <a href="#" class="is-active" style="width:84px">ABOUT US</a>
    <a href="#" style="width:96px">SERVICES</a>
    <a href="#" style="width:108px">PUBLICATIONS</a>
    <a href="#" style="width:68px">BLOG</a>
    <a href="#" style="width:67px">LINKS</a>
    <a href="#" style="width:83px;border-right:none">CONTACT</a>
  </nav>

  <div class="abs hero" role="img" aria-label="Photo of a researcher in a white lab coat working in a laboratory"></div>
  <div class="abs hero-shadow"></div>

  <section>
    <div class="abs service" style="left:50px;top:409px">
      <div class="service-icon">
        <svg width="40" height="40" viewBox="0 0 40 40"><rect x="8" y="6" width="20" height="26" fill="none" stroke="#fff" stroke-width="2"/><path d="M12 12h12M12 17h12M12 22h8" stroke="#fff" stroke-width="2"/><circle cx="28" cy="26" r="5" fill="none" stroke="#1fd0c0" stroke-width="2.5"/><path d="M31.5 29.5l4 4" stroke="#1fd0c0" stroke-width="3"/></svg>
      </div>
      <div class="service-title">RESEARCH ANALYSIS</div>
      <a class="read-more" href="#">Read More</a>
    </div>
    <div class="abs service" style="left:293px;top:409px">
      <div class="service-icon">
        <svg width="40" height="40" viewBox="0 0 40 40"><rect x="8" y="6" width="20" height="26" fill="none" stroke="#fff" stroke-width="2"/><path d="M12 12h12M12 17h12M12 22h8" stroke="#fff" stroke-width="2"/><circle cx="28" cy="26" r="5" fill="none" stroke="#1fd0c0" stroke-width="2.5"/><path d="M31.5 29.5l4 4" stroke="#1fd0c0" stroke-width="3"/></svg>
      </div>
      <div class="service-title">KINSHIP DETERMINATION</div>
      <a class="read-more" href="#">Read More</a>
    </div>
    <div class="abs service" style="left:530px;top:409px">
      <div class="service-icon">
        <svg width="40" height="40" viewBox="0 0 40 40"><rect x="8" y="6" width="20" height="26" fill="none" stroke="#fff" stroke-width="2"/><path d="M12 12h12M12 17h12M12 22h8" stroke="#fff" stroke-width="2"/><circle cx="28" cy="26" r="5" fill="none" stroke="#1fd0c0" stroke-width="2.5"/><path d="M31.5 29.5l4 4" stroke="#1fd0c0" stroke-width="3"/></svg>
      </div>
      <div class="service-title">FORENSIC GENEALOGY</div>
      <a class="read-more" href="#">Read More</a>
    </div>
  </section>

  <div class="abs divider"></div>

  <section>
    <h1 class="abs welcome-title">WELCOME HOLLOW OAK RESEARCH</h1>
    <p class="abs welcome-text">Lorem Ipsum is simply dummy text of the printing and typesetting industry. Lorem Ipsum has been the industry's standard dummy text ever since the 1500s, when an unknown printer took a galley of type and scrambled it to make a type specimen book. It has survived not only five centuries, but also the leap into electronic typesetting, remaining essentially unchanged. It was popularised in the 1960s with the release of Lettersheet sheets containing Lorem Ipsum passages, and more recently with desktop publishing software like PageComposer including versions of Lorem Ipsum.</p>
    <div class="abs map" role="img" aria-label="Street map showing the office location"></div>
    <div class="abs contact-row">
      <svg class="ic" viewBox="0 0 12 12"><rect width="12" height="12" rx="2" fill="var(--teal)"/><path fill="#fff" d="M3.5 2.5h1.5l.6 2-1 .8a5 5 0 0 0 2.1 2.1l.8-1 2 .6v1.5c0 .5-.4.9-.9.9A6.4 6.4 0 0 1 2.6 3.4c0-.5.4-.9.9-.9z"/></svg>
      <span style="width:72px">555-014-2287</span>
      <svg class="ic" viewBox="0 0 12 12"><path fill="var(--teal)" d="M6 1L.5 6H2v5h3V8h2v3h3V6h1.5z"/></svg>
      <span>MARA QUILLEN, PROFESSIONAL GENEALOGIST PO BOX 4471<br>RIVERTON, TX 78000-4471</span>
    </div>
  </section>

  <aside class="abs booking">
    <div class="booking-head">BOOK APPOINTMENT</div>
    <div class="booking-body">
      <div class="field-label">Are you existing parent?</div>
      <div class="radio-row"><span>Yes<i></i></span><span>No<i></i></span></div>
      <div class="input">Name</div>
      <div class="input">Email</div>
      <div class="input">Contact Number</div>
      <div class="field-label" style="margin-top:10px">Preferred date?</div>
      <div class="select-row"><div class="select">Day</div><div class="select">Month</div><div class="select">Month</div></div>
      <div class="field-label">Preferred time?</div>
      <div class="select-row"><div class="select">12</div><div class="select">00</div><div class="select">AM</div></div>
      <div class="book-btn">REQUEST BOOKING</div>
    </div>
  </aside>

  <footer class="abs site-footer">
    <div class="abs quick-links">
      <div class="footer-title">Quick Links</div>
      <ul><li>Home</li><li>About</li><li>Services</li><li>Publications</li><li>Blog</li><li>Contact us</li></ul>
    </div>
    <div class="abs connect">
      <div class="footer-title">Connect with us</div>
      <p>Lorem ipsum dolor sit amet, consectetuer adipiscing elit, sed diam nonummy nibh euismod</p>
      <div class="social"><b></b>Chatterly</div>
      <div class="social"><b></b>Chirper</div>
      <div class="social"><b></b>Linkwork</div>
    </div>
    <div class="abs email-form">
      <div class="footer-title">E-Mail Us</div>
      <div class="f-input">Name</div>
      <div class="f-input">Email</div>
      <div class="f-input tall">Comments</div>
      <div class="submit">SUBMIT</div>
    </div>
  </footer>
  <div class="abs footer-bar">Hollow Oak Research All Rights Reserved © 2014 Privacy policy</div>

</div>
</body>
</html>
```